Building company needs a letterhead design

I'm after a modern but professional letter head.
Must have the below details:
- Logo
- Website - TARVELGROUP.COM.AU
- Email - INFO@TARVELGROUP.COM.AU
- Office - 03 58206317
- Mobile number - 0413865290
- ABN - 47 318 264 105
...........................................................................................................................................................................................................................
- Logo
- Office - 03 58206317
- ABN - 47 318 264 105

Target Market(s)

.

Industry/Entity Type

Construction Company

Font styles to use
Sans Serif

Requirements
Must have
• Must have the below details:
• - Logo
• - Website - TARVELGROUP.COM.AU
• - Email - INFO@TARVELGROUP.COM.AU
• - Office - 03 58206317
• - Mobile number - 0413865290
• - ABN - 47 318 264 105
Nice to have
• .
Should not have
• .

```html
<!DOCTYPE html>
<html lang="en">
<head>
<meta charset="utf-8">
<title>Tarvel Building Group – Letterhead</title>
<link rel="stylesheet" href="https://fonts.googleapis.com/css2?family=Arimo:wght@400;700&display=swap">
<style>
  :root {
    --brand-orange: #fbae00;
    --brand-grey: #555759;
    --ink: #111111;
    --paper: #ffffff;
  }
  * { box-sizing: border-box; margin: 0; padding: 0; }
  html, body {
    width: 849px;
    height: 1200px;
    overflow: hidden;
    background: var(--paper);
  }
  .letterhead {
    position: relative;
    width: 849px;
    height: 1200px;
    background: var(--paper);
    font-family: "Arimo", Arial, sans-serif;
    color: var(--ink);
    overflow: hidden;
  }
  .brand {
    position: absolute;
    top: 30px;
    left: 0;
    width: 849px;
    display: flex;
    justify-content: center;
    align-items: center;
    gap: 14px;
  }
  .brand-mark {
    width: 64px;
    height: 64px;
    background: var(--brand-orange);
  }
  .brand-name {
    font-weight: 700;
    color: var(--brand-grey);
    line-height: 1.05;
  }
  .brand-name .line-main {
    display: block;
    font-size: 32px;
    letter-spacing: 1px;
  }
  .brand-name .line-sub {
    display: block;
    font-size: 13.5px;
    letter-spacing: 1.6px;
    margin-top: 3px;
  }
  .footer-wave {
    position: absolute;
    left: 0;
    top: 0;
    width: 849px;
    height: 1200px;
  }
  .footer-wave path { fill: var(--brand-orange); }
  .contact-list {
    position: absolute;
    left: 530px;
    top: 1040px;
    list-style: none;
    font-size: 16px;
  }
  .contact-list li {
    height: 30px;
    line-height: 30px;
    white-space: nowrap;
  }
  .contact-list .label { font-weight: 700; }
  .contact-list .website { font-size: 18.5px; }
</style>
</head>
<body>
  <main class="letterhead">
    <header class="brand">
      <span class="brand-mark" aria-hidden="true"></span>
      <span class="brand-name">
        <span class="line-main">TARVEL</span>
        <span class="line-sub">BUILDING GROUP</span>
      </span>
    </header>

    <svg class="footer-wave" viewBox="0 0 849 1200" aria-hidden="true">
      <path d="M31 1200 C 150 1100, 330 1062, 530 1044 C 690 1030, 790 1000, 849 948 L 849 1200 Z"/>
    </svg>

    <ul class="contact-list">
      <li><span class="label">Email :</span> info@tarvelgroup.com.au</li>
      <li><span class="label">Mobile No. :</span>&nbsp; 0413865290</li>
      <li><span class="label">Office :</span> 03 58206317</li>
      <li><span class="label">ABN :</span> 47 318 264 105</li>
      <li class="website"><span class="label">Website :</span> tarvelgroup.com.au</li>
    </ul>
  </main>
</body>
</html>
```